Business Card Design needed for logo design project

This project is linked to a href='http://jobs.pixelfennel.example/job.aspx?id=412907'Tide Nook: Design a logo for our new trailer boat syndication business in Sydney
Our company needs a Business Card Design. Please refer to our original project in the link above.
I would like a relatively simple and classy business card design. could you please also use small symbols for identifying contact info eg. mobile, web and email?
Updates
Please see my new project to design a business card for a trailer boat syndication business in Sydney, Australia.
Industry/Entity Type
Business
Look and feel
Each slider illustrates characteristics of the customer's brand and the style your logo design should communicate.

```html
<!DOCTYPE html>
<html lang="en">
<head>
<meta charset="utf-8">
<title>Tide Nook Business Cards</title>
<link href="https://fonts.googleapis.com/css2?family=Open+Sans:wght@400;600;800&display=swap" rel="stylesheet">
<style>
  :root {
    --teal: #2fb0bc;
    --teal-soft: #45bcc6;
    --ink: #1c1c1e;
    --paper: #ffffff;
    --stage: #e9e6e1;
  }
  * { margin: 0; padding: 0; box-sizing: border-box; }
  html, body { width: 1200px; height: 900px; overflow: hidden; }
  body {
    background: var(--stage);
    font-family: "Open Sans", Arial, sans-serif;
    position: relative;
  }
  .card {
    position: absolute;
    left: 280px;
    width: 640px;
    height: 366px;
    border-radius: 22px;
    overflow: hidden;
    box-shadow: 0 10px 28px rgba(0,0,0,0.18);
  }
  /* Back */
  .card-back { top: 50px; background: var(--teal); }
  .back-brand {
    position: absolute;
    top: 40px;
    right: 46px;
    text-align: right;
    color: var(--paper);
  }
  .back-site { font-size: 38px; font-weight: 800; letter-spacing: 0.5px; line-height: 1; }
  .back-tagline { font-size: 12px; font-weight: 800; letter-spacing: 1.6px; margin-top: 8px; }
  /* Front */
  .card-front { top: 484px; background: var(--paper); }
  .front-shape { position: absolute; inset: 0; width: 100%; height: 100%; }
  .front-brand {
    position: absolute;
    top: 48px;
    left: 118px;
    display: flex;
    flex-direction: column;
  }
  .brand-row { display: flex; align-items: center; gap: 12px; }
  .brand-dot { width: 18px; height: 18px; border-radius: 50%; background: var(--teal); }
  .brand-name { font-size: 46px; font-weight: 800; color: var(--teal); line-height: 1; }
  .brand-tagline {
    font-size: 9px; font-weight: 800; color: var(--ink);
    letter-spacing: 1.4px; margin-top: 8px; margin-left: 30px;
  }
  .holder { position: absolute; left: 52px; top: 196px; color: var(--paper); }
  .holder-name { font-size: 24px; font-weight: 600; line-height: 1.1; }
  .holder-role { font-size: 14px; font-weight: 400; }
  .contacts {
    position: absolute; left: 338px; top: 262px;
    list-style: none; color: var(--paper);
    font-size: 16px; line-height: 28px;
  }
  .contacts li { display: flex; align-items: center; gap: 12px; }
  .contacts svg { width: 16px; height: 16px; flex: none; }
</style>
</head>
<body>
  <section class="card card-back" aria-label="Card back">
    <div class="back-brand">
      <div class="back-site">TideNook.com.au</div>
      <div class="back-tagline">TRAILER BOAT SYNDICATION AND MANAGEMENT</div>
    </div>
  </section>

  <section class="card card-front" aria-label="Card front">
    <svg class="front-shape" viewBox="0 0 640 366" preserveAspectRatio="none" aria-hidden="true">
      <polygon points="0,146 640,272 640,366 0,366" fill="var(--teal)"/>
      <polygon points="0,138 640,264 640,278 0,146" fill="var(--ink)"/>
      <polygon points="0,146 640,278 640,284 0,152" fill="var(--paper)"/>
    </svg>

    <div class="front-brand">
      <div class="brand-row">
        <span class="brand-dot"></span>
        <span class="brand-name">Tide Nook</span>
      </div>
      <span class="brand-tagline">TRAILER BOAT SYNDICATION AND MANAGEMENT</span>
    </div>

    <div class="holder">
      <div class="holder-name">Sam Carter</div>
      <div class="holder-role">Director</div>
    </div>

    <ul class="contacts">
      <li>
        <svg viewBox="0 0 16 16" aria-hidden="true"><rect x="4" y="1" width="8" height="14" rx="1.5" fill="none" stroke="currentColor" stroke-width="1.4"/><circle cx="8" cy="12.4" r="0.9" fill="currentColor"/></svg>
        555 210 4478
      </li>
      <li>
        <svg viewBox="0 0 16 16" aria-hidden="true"><rect x="1" y="3" width="14" height="10" fill="none" stroke="currentColor" stroke-width="1.4"/><path d="M1 3 L8 9 L15 3" fill="none" stroke="currentColor" stroke-width="1.4"/></svg>
        info@tidenook.example
      </li>
      <li>
        <svg viewBox="0 0 16 16" aria-hidden="true"><circle cx="8" cy="8" r="6.5" fill="none" stroke="currentColor" stroke-width="1.3"/><ellipse cx="8" cy="8" rx="2.8" ry="6.5" fill="none" stroke="currentColor" stroke-width="1.1"/><path d="M1.5 8 H14.5" stroke="currentColor" stroke-width="1.1"/></svg>
        www.tidenook.example
      </li>
    </ul>
  </section>
</body>
</html>
```